Business Card and Logo Color Scheme Design Contest

We are starting a new company called Lone Ridge Structural Partners and already have a logo however, the colors for the logo itself are not final and COULD be changed. I'm hoping to move AWAYfrom the gold color in the card and the logo as it seems a bit outdated. What we need help with is to find what our business color scheme will be, and then incorporate those colors into both the logo and the business card design itself. We also want to make sure we are known as "LRS" so in the future we can just refer to ourselves as "LRS" and not Lone Ridge Structural Partners. That being said, I would like to make a slight change to the logo to somehow include the letters "LRS." The logo used in the front of the card design MUST ALSO include the words "Firm No. 64307" within the logo. My vision is for the front of the card to have the information shown in the attached image. For the back of the card, I'm hoping to have something very simple. I'm envisioning a solid color with either the website (www.bridgemarkplans.com) and a simplified version of the logo. I've attached an example but I'm looking for a complete redesign. I'm looking for a slick, modern and simple design.

Industry/Entity Type

Civil Engineer

Contact Information for Business Card

Logo
Firm No. 64307
Marcus Holloway, PE
Chief Operating Officer
Email:mholloway@bridgemarkplans.com
Ph: 312.555.0142 | D: 312.555.0178 | M:515.555.0263
4187 W. Kellingham, Alder Flats, Nevada 89502
www.bridgemarkplans.com

Requirements
Must have
• Logo
Contact Info
Nice to have
• "LRS" Incorporated in the design
Should not have
• The current color scheme

```html
<!DOCTYPE html>
<html lang="en">
<head>
<meta charset="utf-8">
<title>Lone Ridge Structural Partners – Business Card</title>
<link href="https://fonts.googleapis.com/css2?family=Libre+Baskerville&family=Mulish:wght@400;500&display=swap" rel="stylesheet">
<style>
  :root {
    --backdrop: #cfcfcf;
    --orange: #d6502a;
    --navy: #22283f;
    --navy-light: #2c3658;
    --paper: #f7f7f6;
    --ink: #1e1f24;
    --grey-text: #6d6f75;
    --white: #ffffff;
  }
  * { margin: 0; padding: 0; box-sizing: border-box; }
  html, body { width: 1200px; height: 1200px; overflow: hidden; background: var(--backdrop); }
  .canvas { position: relative; width: 1200px; height: 1200px; }
  .card { position: absolute; top: 287px; width: 356px; height: 622px; overflow: hidden; }

  /* Back side */
  .card-back { left: 170px; background: var(--orange); }
  .back-mark {
    position: absolute; left: 0; width: 100%; top: 238px;
    text-align: center; color: var(--white);
    font-family: "Libre Baskerville", serif; font-size: 72px; letter-spacing: 2px;
  }
  .back-url {
    position: absolute; left: 0; width: 100%; top: 548px; text-align: center;
    color: var(--white); font-family: "Libre Baskerville", serif; font-size: 15px;
  }
  .back-band { position: absolute; bottom: 0; height: 24px; width: 50%; }
  .back-band.left { left: 0; background: var(--navy); }
  .back-band.right { right: 0; background: var(--navy-light); }

  /* Front side */
  .card-front { left: 677px; background: var(--paper); font-family: "Mulish", sans-serif; }
  .logo-square { position: absolute; left: 34px; top: 84px; width: 52px; height: 52px; background: var(--orange); }
  .logo-name {
    position: absolute; right: 33px; top: 70px; text-align: right; font-weight: 400;
    font-family: "Libre Baskerville", serif; color: var(--navy); line-height: 1.25;
  }
  .logo-name .line-one { display: block; font-size: 25px; }
  .logo-name .line-two { display: block; font-size: 16px; }
  .firm-no {
    position: absolute; right: 33px; top: 164px; display: flex; align-items: center; gap: 6px;
    font-family: "Libre Baskerville", serif; font-size: 12px; color: var(--navy);
  }
  .firm-no::before { content: ""; width: 78px; height: 1px; background: var(--navy); }
  .split-band { position: absolute; top: 234px; height: 17px; }
  .split-band.navy { left: 0; width: 178px; background: var(--navy); }
  .split-band.orange { left: 178px; width: 178px; background: var(--orange); }
  .person-tab {
    position: absolute; left: 282px; top: 251px; width: 53px; height: 80px;
    background: var(--orange); display: flex; align-items: center; justify-content: center;
  }
  .person-name { position: absolute; right: 90px; top: 280px; font-size: 23px; color: var(--ink); font-weight: 500; white-space: nowrap; }
  .person-title { position: absolute; right: 90px; top: 310px; font-size: 15.5px; color: var(--grey-text); white-space: nowrap; letter-spacing: 0.2px; }
  .contact-rail {
    position: absolute; left: 20px; top: 405px; width: 53px; height: 217px;
    background: linear-gradient(to bottom, var(--navy-light), #171b2b);
  }
  .contact-icon { position: absolute; left: 37px; width: 20px; height: 20px; }
  .contact-text { position: absolute; left: 86px; font-size: 16px; color: var(--ink); line-height: 20px; letter-spacing: 0.4px; white-space: nowrap; }
  .contact-text.email { font-size: 15px; letter-spacing: -0.2px; }
</style>
</head>
<body>
<main class="canvas">
  <section class="card card-back" aria-label="Card back">
    <div class="back-mark">LRS</div>
    <p class="back-url">WWW.BRIDGEMARKPLANS.COM</p>
    <div class="back-band left"></div>
    <div class="back-band right"></div>
  </section>

  <section class="card card-front" aria-label="Card front">
    <div class="logo-square"></div>
    <h1 class="logo-name"><span class="line-one">LONE RIDGE</span><span class="line-two">STRUCTURAL PARTNERS</span></h1>
    <p class="firm-no">Firm No. 64307</p>

    <div class="split-band navy"></div>
    <div class="split-band orange"></div>

    <div class="person-tab">
      <svg width="26" height="26" viewBox="0 0 26 26" aria-hidden="true">
        <circle cx="13" cy="9" r="5.5" fill="#fff"/>
        <path d="M3 24c0-6 4.5-9 10-9s10 3 10 9z" fill="#fff"/>
      </svg>
    </div>
    <p class="person-name">Marcus Holloway, PE</p>
    <p class="person-title">CHIEF OPERATING OFFICER</p>

    <div class="contact-rail"></div>
    <svg class="contact-icon" style="top:425px" viewBox="0 0 20 20" aria-hidden="true">
      <rect x="5" y="1" width="10" height="18" rx="2" fill="none" stroke="#fff" stroke-width="1.6"/>
      <circle cx="10" cy="15.5" r="1" fill="#fff"/>
    </svg>
    <svg class="contact-icon" style="top:469px" viewBox="0 0 20 20" aria-hidden="true">
      <path d="M4 2l3 0 2 5-2 1.5c1 2.3 2.7 4 5 5L13.5 11l5 2v3c0 1-1 2-2 2C9 18 2 11 2 4c0-1 1-2 2-2z" fill="#fff"/>
    </svg>
    <svg class="contact-icon" style="top:509px" viewBox="0 0 20 20" aria-hidden="true">
      <rect x="1" y="4" width="18" height="12" fill="#fff"/>
      <path d="M1 4l9 7 9-7M1 16l7-6M19 16l-7-6" fill="none" stroke="#22283f" stroke-width="1.3"/>
    </svg>
    <svg class="contact-icon" style="top:549px" viewBox="0 0 20 20" aria-hidden="true">
      <path d="M10 1c-3.9 0-6.5 2.8-6.5 6.3C3.5 12 10 19 10 19s6.5-7 6.5-11.7C16.5 3.8 13.9 1 10 1z" fill="#fff"/>
      <circle cx="10" cy="7.3" r="2.4" fill="#22283f"/>
    </svg>

    <p class="contact-text" style="top:425px">515.555.0263</p>
    <p class="contact-text" style="top:459px">312.555.0142<br>312.555.0178</p>
    <p class="contact-text email" style="top:509px">mholloway@bridgemarkplans.com</p>
    <p class="contact-text" style="top:546px;left:90px">4187 W. Kellingham,<br>Alder Flats, Nevada 89502</p>
  </section>
</main>
</body>
</html>
```